Broschüre für ein Immobilienunternehmen
Zielgruppe
Wir sind ein junges und modernes Immobilienunternehmen, dass sich auf den Verkauf und die Vermietung von Immobilien und Grundstücken und Beratung deren Eigentümer fokussiert. Als Zielgruppe definieren wir alle Personen im geschäfts- und erwerbsfähigem Alter (ca. 21-80 Jahre) sowie vor allem auch Eigentümer einer Immobilie/eines Grundstückes.
Die Broschüre wird in mehr als 10.000 Haushalten zu sehen sein.
Aufgabenstellung
Wir suchen ein modernes aber auch hochwertiges/seriöses Design und legen vor allem Wert auf ein vertrauensvolles Auftreten mit modernen Elementen. Die Broschüre wird in mehr als 10.000 Haushalten zu sehen sein und soll einen Wiedererkennungswert bieten, der auf die Firma sowie auf die Social Media Kampagnen zurück zu führen ist.
Der Text für das Cover soll zum einen die Interessen eines potentiellen Verkäufers einer Immobilien anregen, zum anderen soll mit dem Slogan geworben werden: 'Garantierte Courtage von 1,8% zzgl. MwSt., wenn Sie bis zum 01.05.2022 Ihre Immobilie über Korff - ter Haaken Immobilien GbR veräußern lassen'
Innerhalb der Seiten kann gerne mit einem Mix, sowohl aus Unternehmensvorstellung, Referenzen sowie Leistungen, als auch Bildimpressionen einiger Immobilien und Texte von der Webseite gearbeitet werden.
Wichtig:
- 8 Seiten Broschüre
- 8 Seiten Design
- Eckdaten werden als Daten angehangen.

```html
<!DOCTYPE html>
<html lang="de">
<head>
<meta charset="utf-8">
<title>Broschüre – Innenseiten</title>
<link rel="stylesheet" href="https://fonts.googleapis.com/css2?family=Lato:wght@400;700&family=Ubuntu:wght@400;500&display=swap">
<style>
  :root {
    --bg: #e4e4e4;
    --paper: #ffffff;
    --gold: #c28f2a;
    --gold-light: #dcb25a;
    --gold-dark: #b7841f;
    --ink: #3a3a3a;
    --ink-soft: #555555;
    --white: #ffffff;
  }
  * { margin: 0; padding: 0; box-sizing: border-box; }
  html, body { width: 1200px; height: 864px; overflow: hidden; }
  body {
    background: var(--bg);
    font-family: "Lato", Arial, sans-serif;
    color: var(--ink);
    position: relative;
  }
  .spread {
    position: absolute;
    left: 30px; top: 22px;
    width: 1140px; height: 820px;
    display: flex;
    box-shadow: 0 10px 30px rgba(0,0,0,.18);
  }
  .page { width: 570px; height: 820px; position: relative; overflow: hidden; background: var(--paper); }
  .photo { position: absolute; left: 0; top: 0; width: 100%; height: 420px; }
  .photo--meeting-room { background: linear-gradient(160deg, #f1efec 0%, #e2ddd6 45%, #b49a7c 100%); }
  .photo--team { background: linear-gradient(150deg, #dcdbf0 0%, #eceae8 40%, #cfd0d2 75%, #9aa1ab 100%); height: 440px; }

  .gold-panel {
    position: absolute; left: 0; top: 420px; width: 100%; height: 400px;
    background: radial-gradient(ellipse at 55% 40%, var(--gold-light) 0%, var(--gold) 55%, var(--gold-dark) 100%);
    color: var(--white);
    padding: 34px 38px 0;
  }
  .stats { display: flex; justify-content: space-between; text-align: center; }
  .stat { width: 160px; }
  .stat__icon {
    width: 70px; height: 56px; border-radius: 50%;
    background: var(--white); margin: 0 auto 12px;
    display: flex; align-items: center; justify-content: center;
  }
  .stat__value { font-family: "Ubuntu", sans-serif; font-weight: 500; font-size: 17px; }
  .stat__label { font-size: 10.5px; line-height: 1.3; }
  .gold-panel h2 {
    font-family: "Ubuntu", sans-serif; font-weight: 400;
    font-size: 33px; margin: 30px 0 12px; letter-spacing: .5px;
  }
  .gold-panel p { font-size: 11.5px; line-height: 1.45; margin-bottom: 14px; max-width: 480px; }

  .content { position: absolute; left: 40px; right: 36px; top: 476px; }
  .content h2 {
    font-family: "Ubuntu", sans-serif; font-weight: 400; font-size: 27px;
    line-height: 1.2; color: var(--ink);
  }
  .accent { color: var(--gold); }
  .content h3 {
    font-family: "Ubuntu", sans-serif; font-weight: 400; font-size: 17px;
    line-height: 1.3; margin: 16px 0 22px; color: var(--ink);
  }
  .content p { font-size: 11px; line-height: 1.55; color: var(--ink-soft); margin-bottom: 12px; }
</style>
</head>
<body>
<div class="spread">
  <section class="page page--left">
    <div class="photo photo--meeting-room" role="img" aria-label="Foto: heller Besprechungsraum mit ovalem weißem Tisch, Stühlen, Fenstern und Pflanzen"></div>
    <div class="gold-panel">
      <div class="stats">
        <div class="stat">
          <div class="stat__icon">
            <svg width="34" height="28" viewBox="0 0 34 28"><path d="M3 14 L17 3 L31 14 M7 12 V26 H27 V12" fill="none" stroke="#c28f2a" stroke-width="3"/><rect x="14" y="17" width="6" height="9" fill="#c28f2a"/></svg>
          </div>
          <div class="stat__value">+ 11,000m²</div>
          <div class="stat__label">Wohn- &amp; Gewerbeflächen<br>im Portfolio</div>
        </div>
        <div class="stat">
          <div class="stat__icon">
            <svg width="36" height="28" viewBox="0 0 36 28" fill="none" stroke="#c28f2a" stroke-width="2"><circle cx="18" cy="8" r="4"/><path d="M10 24 C10 16 26 16 26 24"/><circle cx="8" cy="12" r="3"/><path d="M2 25 C2 19 12 19 12 22"/><circle cx="28" cy="12" r="3"/><path d="M34 25 C34 19 24 19 24 22"/></svg>
          </div>
          <div class="stat__value">+ 30,000</div>
          <div class="stat__label">mtl. Exposébesuche</div>
        </div>
        <div class="stat">
          <div class="stat__icon">
            <svg width="32" height="26" viewBox="0 0 32 26"><path d="M4 5 H22 V16 A6 6 0 0 1 16 22 H10 A6 6 0 0 1 4 16 Z" fill="#c28f2a"/><path d="M22 8 H26 A3 3 0 0 1 26 15 H22" fill="none" stroke="#c28f2a" stroke-width="3"/></svg>
          </div>
          <div class="stat__value">160+</div>
          <div class="stat__label">mtl. Kaffeetassen Bedarf</div>
        </div>
      </div>
      <h2>Unsere Kompetenz, Ihr Vorteil.</h2>
      <p>Beim Verkaufen und Vermieten von Immobilien geht es nicht nur um den Preis, sondern um Service, Liebe und Energie.</p>
      <p>Partner an Ihrer Seite rund um das Thema Immobilien. Mit geschäftsmäßigen Fingerspitzengefühl, weit gefächertem Netzwerk und Humor sind wir DER Immobilienmakler aus Moers.</p>
    </div>
  </section>

  <section class="page page--right">
    <div class="photo photo--team" role="img" aria-label="Foto: zwei Geschäftsführer am runden Besprechungstisch vor einem Bildschirm"></div>
    <div class="content">
      <h2>Von Ehrgeiz angetrieben, durch<br><span class="accent">Leidenschaft</span> vereint.</h2>
      <h3><span class="accent">Effiziente &amp; nachhaltige Vermietung</span> von Bestands- &amp; Neubauobjekten deutschlandweit aus einer Hand.</h3>
      <p>Sie sind Privatinvestor*in, eine Immobiliengesellschaft, eine Kapitalverwaltungsgesellschaft, eine Immobilienfonds- und Vermögensverwaltungsgesellschaft oder im Bereich Asset Management tätig und benötigen eine innovative Unternehmensgruppe für das Portfolio-Management, technisches Gebäudemanagment sowie eine nachhaltige und effiziente Begleitung in den Bereichen Vermietung und Verkauf?</p>
      <p>Wir freuen uns über einen persönlichen und ideenreichen Austausch mit Ihnen.</p>
    </div>
  </section>
</div>
</body>
</html>
```